Marlow Fields Thank-You Tag

Looking for a file that incorporates current branding/colors and says:

"Thanks for Swimming with Us!"
Marlow Fields Otters

Samples of other pieces we've done recently are attached.

Will be printed on cardstock that is
Width: 3.5 inches
Height: 2.5 inches

```html
<!DOCTYPE html>
<html lang="en">
<head>
<meta charset="utf-8">
<title>Marlow Fields Otters – Thank-You Tag</title>
<link rel="stylesheet" href="https://fonts.googleapis.com/css2?family=Fredoka:wght@500;600;700&display=swap">
<style>
  :root {
    --team-blue: #2a4f9e;
    --team-pink: #ee5fa1;
    --water-blue: #8dbce6;
    --silver: #c3c4c6;
    --white: #ffffff;
    --backdrop: #3a3938;
  }
  * { margin: 0; padding: 0; box-sizing: border-box; }
  html, body {
    width: 1200px;
    height: 901px;
    overflow: hidden;
    background: var(--backdrop);
  }
  .tag-frame {
    position: absolute;
    left: 20px;
    top: 36px;
    width: 1160px;
    height: 828px;
    overflow: hidden;
  }
  .tag {
    position: absolute;
    left: 0;
    top: 0;
    width: 1590px;
    height: 1135px;
    transform: scale(0.7296);
    transform-origin: 0 0;
    background: var(--team-blue);
    font-family: "Fredoka", sans-serif;
    font-weight: 600;
    color: var(--white);
    overflow: hidden;
  }
  .headline-line {
    position: absolute;
    left: 113px;
    line-height: 1;
    white-space: nowrap;
  }
  .headline-thanks { top: 80px; font-size: 118px; font-weight: 700; letter-spacing: -1px; }
  .headline-for { font-size: 62px; font-weight: 700; margin-left: 14px; }
  .headline-swimming { top: 166px; left: 106px; font-size: 160px; font-weight: 700; color: var(--team-pink); letter-spacing: 1px; }
  .headline-with { top: 313px; font-size: 118px; font-weight: 700; letter-spacing: -1px; }

  .squiggle { position: absolute; left: 110px; top: 495px; width: 630px; height: 40px; }

  .team-place { position: absolute; left: 107px; top: 572px; font-size: 70px; line-height: 1; font-weight: 600; white-space: nowrap; }
  .team-mascot { position: absolute; left: 107px; top: 638px; font-size: 97px; line-height: 1; font-weight: 600; color: var(--team-pink); white-space: nowrap; }

  .year-digit { position: absolute; font-size: 290px; line-height: 1; font-weight: 700; }
  .year-two-top { left: 1150px; top: 44px; }
  .year-two-bottom { left: 1212px; top: 230px; }
  .year-six { left: 1340px; top: 292px; color: var(--team-pink); }
  .year-zero { position: absolute; left: 1300px; top: 92px; width: 236px; height: 236px; }
  .club-name {
    position: absolute;
    left: 1348px;
    top: 180px;
    width: 140px;
    text-align: center;
    font-size: 19px;
    line-height: 1.15;
    font-weight: 600;
    color: var(--white);
  }

  .waves { position: absolute; left: 0; top: 0; width: 1590px; height: 1135px; }

  .leaping-mascot {
    position: absolute;
    left: 843px;
    top: 515px;
    width: 430px;
    height: 495px;
    border-radius: 50%;
    background: radial-gradient(ellipse at center, var(--silver) 0%, rgba(195,196,198,0.55) 55%, rgba(195,196,198,0) 75%);
  }
</style>
</head>
<body>
  <div class="tag-frame">
    <div class="tag">
      <svg class="waves" viewBox="0 0 1590 1135" aria-hidden="true">
        <path fill="#ffffff" d="M0,838 q67.5,-20 135,0 t135,0 t135,0 t135,0 t135,0 t135,0 t135,0 t135,0 t135,0 t135,0 t135,0 t135,0 V1135 H0 Z"/>
        <path fill="#8dbce6" d="M0,888 q67.5,-20 135,0 t135,0 t135,0 t135,0 t135,0 t135,0 t135,0 t135,0 t135,0 t135,0 t135,0 t135,0 V1135 H0 Z"/>
        <path fill="#ffffff" d="M0,948 q67.5,-20 135,0 t135,0 t135,0 t135,0 t135,0 t135,0 t135,0 t135,0 t135,0 t135,0 t135,0 t135,0 V1135 H0 Z"/>
        <path fill="#ee5fa1" d="M0,962 q67.5,-20 135,0 t135,0 t135,0 t135,0 t135,0 t135,0 t135,0 t135,0 t135,0 t135,0 t135,0 t135,0 V1135 H0 Z"/>
      </svg>

      <div class="leaping-mascot" role="img" aria-label="Illustration of the team mascot leaping out of the water"></div>

      <h1 class="headline">
        <span class="headline-line headline-thanks">THANKS<span class="headline-for">FOR</span></span>
        <span class="headline-line headline-swimming">SWIMMING</span>
        <span class="headline-line headline-with">WITH US!</span>
      </h1>

      <svg class="squiggle" viewBox="0 0 630 40" aria-hidden="true">
        <path d="M4,20 q19.5,-14 39,0 t39,0 t39,0 t39,0 t39,0 t39,0 t39,0 t39,0 t39,0 t39,0 t39,0 t39,0 t39,0 t39,0 t39,0 t39,0" fill="none" stroke="#ee5fa1" stroke-width="6" stroke-linecap="round"/>
      </svg>

      <p class="team-place">MARLOW FIELDS</p>
      <p class="team-mascot">OTTERS</p>

      <div class="season-year" aria-label="2026">
        <span class="year-digit year-two-top">2</span>
        <svg class="year-zero" viewBox="0 0 236 236" aria-hidden="true">
          <circle cx="118" cy="118" r="90" fill="none" stroke="#ffffff" stroke-width="40"/>
          <circle cx="118" cy="118" r="64" fill="none" stroke="#ffffff" stroke-width="3"/>
        </svg>
        <span class="year-digit year-two-bottom">2</span>
        <span class="year-digit year-six">6</span>
        <p class="club-name">MARLOW FIELDS SWIM</p>
      </div>
    </div>
  </div>
</body>
</html>
```